Web Design Project (Renewable Energy Services Company)

Hello crowd,

We are looking to create a website for a new company. We would like to have the page already coded, if you do not provide the code as well, please indicate so. I am including a very preliminary approximation of the wireframe.

We do not have the logo either the color pallet, however we have in mind couple websites that would be similar tho these.

http://www.brivolen.com/en/

and

http://www.tarmuvex.com/

We did an approximated wireframe our our website, not necesarly to decide on the layout but rather to know how many pages will be needed. It would be around 10 pages. We will need a section that will be an e-commerce page to sell products such as engineering instrumentation, software and consumables such as cable and connectors.

Our company will be called ORVIK. We will be based in Monterrey, Mexico. Our focused will be the development of renewable energy projects. Similar scope of services than http://www.brivolen.com/en/ but only for wind and solar projects.

We like something minimalistic. Some of the things that the logo might or might not include would be the monterrey famous hill, but not strictly necessary.
http://en.plavorinet.org/wiki/Loma_del_Trueno

also ORVIK (which stands for ORganica VIKtoria) the name is similar the bird (seagal) or wind turbines and sun...any of these are only suggestions and we are open to receive any proposals.

There must be a
home page
services page (some subsections)
products page (some subsections)
contact page with contact form

and some additional subsections like careers and partnerships.

We are very excited to start hearing about this project.
Updates

Please for the logo, do not restrict your ideas to the ones provided as it has generated too specific logos. Pleae just allow your imagination to flow for a company that develops renewable energy projects.

Target Market(s)

large companies interested in developing renewable energy projects

Industry/Entity Type

E-Commerce

Requirements
Must have
• Minimalistic and unique design.
Nice to have
• contact form to save contacts in a database

Should not have
• We are looking a very minimalistic logo. It should not be an explicit wind turbine a seagal or anything like that. we are looking for abstract, simple and minimalistic image.

```html
<!DOCTYPE html>
<html lang="en">
<head>
<meta charset="utf-8">
<title>ORVIK</title>
<link rel="stylesheet" href="https://fonts.googleapis.com/css2?family=Lusitana:wght@400;700&family=PT+Sans+Narrow:wght@400;700&display=swap">
<style>
  :root{
    --topbar:#0c2c55;
    --header:#1f62b3;
    --logo-text:#dde6f2;
    --search:#c8ddf6;
    --nav-light:#f7f7f7;
    --nav-dark:#cfcfcf;
    --nav-text:#1a1a1a;
    --page-top:#e8f1fc;
    --page-bottom:#ffffff;
    --card-border:#c9ced6;
    --card-inner:#f4f4f4;
    --title:#2a62a8;
    --body:#444a52;
    --footer:#c6ddf5;
    --footer-link:#2b4d78;
    --footer-small:#6a8ab2;
  }
  *{margin:0;padding:0;box-sizing:border-box}
  html,body{width:1200px;height:1071px;overflow:hidden}
  body{position:relative;background:linear-gradient(var(--page-top) 343px,var(--page-bottom) 900px);font-family:"PT Sans Narrow",sans-serif}
  .abs{position:absolute}

  .topbar{left:0;top:0;width:1200px;height:39px;background:var(--topbar)}
  .topbar span{position:absolute;top:12px;font-weight:700;font-size:15px;letter-spacing:1px;color:#d7e2f0}

  .header{left:0;top:39px;width:1200px;height:304px;background:var(--header)}
  .brand{left:35px;top:61px;display:flex;align-items:center;gap:14px}
  .brand-mark{width:88px;height:88px;border-radius:50%;background:#17406f}
  .brand-name{font-family:"Lusitana",serif;font-weight:700;font-size:68px;letter-spacing:6px;color:var(--logo-text)}

  .search{left:827px;top:90px;width:311px;height:33px;background:var(--search)}
  .search span{position:absolute;left:13px;top:8px;font-family:"Lusitana",serif;font-size:15px;letter-spacing:1px;color:#f4f8fd}
  .search svg{position:absolute;right:-4px;top:-10px}

  .nav{left:61px;top:179px;width:1083px;height:53px;border-radius:8px;background:linear-gradient(var(--nav-light),var(--nav-dark));box-shadow:0 1px 3px rgba(0,0,0,.3)}
  .nav-item{position:absolute;top:12px;height:32px;border-radius:7px;border:1px solid #f0f0f0;background:linear-gradient(#e6e6e6,#d6d6d6);font-family:"Lusitana",serif;font-weight:700;font-size:21px;letter-spacing:2px;color:var(--nav-text);display:flex;align-items:center;justify-content:center;gap:8px}
  .social{position:absolute;top:9px;width:33px;height:33px;border-radius:50%;border:2px solid #e9e9e9}

  .slide{left:87px;top:232px;width:1041px;height:500px;background:linear-gradient(#7aa2d4 0%,#b5cde6 30%,#5b6f4c 55%,#3f5232 75%,#8c8c82 100%)}
  .arrow{top:393px}

  .card{top:663px;width:302px;height:270px;background:#fff;border:1px solid var(--card-border);box-shadow:0 14px 22px -6px rgba(0,0,0,.35)}
  .card-inner{position:absolute;left:11px;top:11px;right:11px;bottom:11px;background:var(--card-inner);padding:14px 10px 0 8px}
  .card h2{font-weight:400;font-size:27px;color:var(--title);text-align:center;letter-spacing:-.3px;margin-bottom:8px}
  .card p{font-size:14.5px;line-height:27px;color:var(--body)}
  .more{position:absolute;right:14px;bottom:12px;display:flex;align-items:center;gap:8px;font-size:20px;color:var(--title)}
  .more i{width:36px;height:36px;border-radius:50%;background:radial-gradient(circle at 40% 30%,#8a8a8a,#333);display:flex;align-items:center;justify-content:center}

  .footer{left:0;top:970px;width:1200px;height:101px;background:var(--footer)}
  .footer a{position:absolute;text-decoration:none;letter-spacing:1px}
  .foot-nav{top:26px;font-weight:700;font-size:16px;color:var(--footer-link)}
  .foot-small{top:57px;font-family:"Lusitana",serif;font-weight:700;font-size:12.5px;color:var(--footer-small)}
</style>
</head>
<body>
  <div class="abs topbar">
    <span style="left:848px">Welcome, Guest</span>
    <span style="left:1001px">LOGIN</span>
    <span style="left:1066px">REGISTER</span>
  </div>

  <div class="abs header"></div>
  <div class="abs brand"><div class="brand-mark"></div><div class="brand-name">ORVIK</div></div>

  <div class="abs search"><span>Search</span>
    <svg width="44" height="44" viewBox="0 0 44 44"><circle cx="18" cy="18" r="12" fill="#bfe6fb" stroke="#2a9fe0" stroke-width="4"/><line x1="27" y1="27" x2="38" y2="38" stroke="#1b86c9" stroke-width="6" stroke-linecap="round"/></svg>
  </div>

  <nav class="abs nav">
    <div class="nav-item" style="left:20px;width:131px">Home</div>
    <div class="nav-item" style="left:171px;width:131px">Services</div>
    <div class="nav-item" style="left:321px;width:161px">Products
      <svg width="12" height="16" viewBox="0 0 12 16"><path d="M1 1 L11 8 L1 15 Z" fill="#3a2a1a"/></svg></div>
    <div class="nav-item" style="left:500px;width:160px">Contact Us</div>
    <div class="social" style="left:906px;background:#1f8fd1"></div>
    <div class="social" style="left:959px;background:#2a4c8a"></div>
    <div class="social" style="left:1011px;background:#e8741a"></div>
  </nav>

  <svg class="abs arrow" style="left:56px" width="31" height="93" viewBox="0 0 31 93"><path d="M31 0 L0 46 L31 93 Z" fill="#dcdcdc"/></svg>
  <svg class="abs arrow" style="left:1128px" width="31" height="93" viewBox="0 0 31 93"><path d="M0 0 L31 46 L0 93 Z" fill="#dcdcdc"/></svg>
  <div class="abs slide" role="img" aria-label="Photo of Loma del Trueno mountain rising above the city under a blue sky"></div>

  <article class="abs card" style="left:98px"><div class="card-inner">
    <h2>Engineering Instrumentation</h2>
    <p>Lorem ipsum dolor sit amet, consectetuer adipiscing elit. Nunc suscipit. Suspendisse enim arcu, convallis non, cursus sed, dignissim et, est. Aenean semper aliquet libero. In ante velit, cursus ut, ultrices vitae, tempor ut, risus. Duis pulvinar.</p>
    <a class="more"><i><svg width="16" height="12" viewBox="0 0 16 12"><path d="M1 1 L8 6 L1 11Z M8 1 L15 6 L8 11Z" fill="#fff"/></svg></i>Read More</a>
  </div></article>

  <article class="abs card" style="left:461px"><div class="card-inner">
    <h2>Software and Consumables</h2>
    <p>Lorem ipsum dolor sit amet, consectetuer adipiscing elit. Nunc suscipit. Suspendisse enim arcu, convallis non, cursus sed, dignissim et, est. Aenean semper aliquet libero. In ante velit, cursus ut, ultrices vitae, tempor ut, risus. Duis pulvinar.</p>
    <a class="more"><i><svg width="16" height="12" viewBox="0 0 16 12"><path d="M1 1 L8 6 L1 11Z M8 1 L15 6 L8 11Z" fill="#fff"/></svg></i>Read More</a>
  </div></article>

  <article class="abs card" style="left:816px"><div class="card-inner">
    <h2>Cable and Connectors</h2>
    <p>Lorem ipsum dolor sit amet, consectetuer adipiscing elit. Nunc suscipit. Suspendisse enim arcu, convallis non, cursus sed, dignissim et, est. Aenean semper aliquet libero. In ante velit, cursus ut, ultrices vitae, tempor ut, risus. Duis pulvinar.</p>
    <a class="more"><i><svg width="16" height="12" viewBox="0 0 16 12"><path d="M1 1 L8 6 L1 11Z M8 1 L15 6 L8 11Z" fill="#fff"/></svg></i>Read More</a>
  </div></article>

  <footer class="abs footer">
    <a class="foot-nav" style="left:443px">Home</a>
    <a class="foot-nav" style="left:532px">Services</a>
    <a class="foot-nav" style="left:631px">Products</a>
    <a class="foot-nav" style="left:738px">Contact Us</a>
    <a class="foot-small" style="left:357px">Copyright © 2012 BRIVOLEN, Inc. All Rights Reserved</a>
    <a class="foot-small" style="left:730px">Terms of Use</a>
    <a class="foot-small" style="left:850px">Privacy Policy</a>
  </footer>
</body>
</html>
```